Business Card Design - Photographer

I am a landscape photographer and I require a business card design. 

I require two designs:
1)  a double sided business card
 and
b)  a single sided business card 

The single sided design can either be the same as the double sided (with just one side having all the information)....or it can be an entire new design. Its up to you.

My corporate colours are (CMYK):

Blue   69, 32, 0, 0
Grey  72,  64,  47,  31
Green  32,  2,  91,  0
Yellow   0, 19, 92, 0
Orange  0, 39, 75, 0

Colour space in final file should be in CMYK.

The details that need to be included on the card:

- Use the provided Logo
- Name: Lukas Wendrovski
- Email:   sales@vistaplume.com.au
- Website:    vistaplume.com.au
- Chirpline:    twitter.com/vistaplume
- Friendpage:   facebook.com/vistaplume
- Mobile  0415 309 662

Please use the attached template to design the logo to the specified size, including the marked bleed lines. I have also attached my logo in PNG (transparent background) and ai format for you to use.

The final file should be:
- Photoshop version with layers so I can edit the name/text etc. All non vector files should be high resolution at 1039 x 697 pixels at 300 dpi.

I also require a file as:
- Vector based PDF

Anyway questions please contact me.

Thank you

Industry/Entity Type

Landscape

Logo styles of interest
Pictorial/Combination Logo
Abstract Logo
Wordmark Logo
Lettermark Logo
Requirements
Must have
• The details that need to be included on the card:

- Use the provided Logo
- Name: Lukas Wendrovski
- Email: sales@vistaplume.com.au
- Website: vistaplume.com.au
- Chirpline: twitter.com/vistaplume
- Friendpage: facebook.com/vistaplume
- Mobile 0415 309 662

```html
<!DOCTYPE html>
<html lang="en">
<head>
<meta charset="utf-8">
<title>Vista Plume – Business Card</title>
<link href="https://fonts.googleapis.com/css2?family=Cinzel:wght@400;500;600&family=Crimson+Text:wght@400;700&display=swap" rel="stylesheet">
<style>
  :root {
    --backdrop: #9a5a2e;
    --card-dark: #3f4050;
    --card-light: #ffffff;
    --ink: #3f4050;
    --ink-soft: #4a4b58;
    --paper-text: #f2f2f5;
  }
  * { margin: 0; padding: 0; box-sizing: border-box; }
  html, body {
    width: 1035px; height: 1200px; overflow: hidden;
    background: var(--backdrop);
  }
  .card {
    position: absolute; left: 145px; width: 744px; height: 486px;
  }
  .card--front { top: 89px; background: var(--card-dark); }
  .card--back { top: 625px; background: var(--card-light); }

  .wordmark {
    position: absolute; left: 0; right: 0; text-align: center;
    font-family: "Cinzel", serif; font-weight: 600;
  }
  .wordmark__name { display: block; white-space: nowrap; }
  .wordmark__rule { display: block; margin: 0 auto; }
  .wordmark__tagline { display: block; white-space: nowrap; font-weight: 600; }

  .card--front .wordmark { top: 190px; color: var(--paper-text); }
  .card--front .wordmark__name { font-size: 58px; letter-spacing: 3px; line-height: 60px; }
  .card--front .wordmark__rule { width: 565px; height: 2px; background: var(--paper-text); margin-top: 3px; }
  .card--front .wordmark__tagline { font-size: 23px; letter-spacing: 3.5px; line-height: 26px; margin-top: 12px; }

  .brand-dot {
    position: absolute; left: 322px; top: 38px; width: 100px; height: 100px;
    border-radius: 50%; background: var(--card-dark);
  }
  .card--back .wordmark { top: 174px; color: var(--ink); }
  .card--back .wordmark__name { font-size: 35px; letter-spacing: 1.5px; line-height: 38px; }
  .card--back .wordmark__rule { width: 340px; height: 1.5px; background: var(--ink); margin-top: 2px; }
  .card--back .wordmark__tagline { font-size: 14px; letter-spacing: 2px; line-height: 16px; margin-top: 8px; }

  .contact {
    position: absolute; font-family: "Crimson Text", serif; color: var(--ink-soft);
    font-size: 23px; line-height: 1; white-space: nowrap;
    display: flex; align-items: center;
  }
  .contact__name {
    position: absolute; left: 31px; top: 313px;
    font-family: "Crimson Text", serif; font-weight: 700; font-size: 37px; color: var(--ink);
  }
  .contact__icon { width: 17px; height: 17px; margin-right: 8px; flex: none; }
  .contact--social-a { left: 29px; top: 370px; }
  .contact--social-b { left: 29px; top: 414px; }
  .contact--phone { left: 398px; top: 327px; }
  .contact--email { left: 398px; top: 372px; }
  .contact--web { left: 398px; top: 415px; }
  .social-square { fill: var(--ink); }
</style>
</head>
<body>
  <section class="card card--front">
    <div class="wordmark">
      <span class="wordmark__name">VISTA PLUME</span>
      <span class="wordmark__rule"></span>
      <span class="wordmark__tagline">FINE ART PHOTOGRAPHY</span>
    </div>
  </section>

  <section class="card card--back">
    <div class="brand-dot"></div>
    <div class="wordmark">
      <span class="wordmark__name">VISTA PLUME</span>
      <span class="wordmark__rule"></span>
      <span class="wordmark__tagline">FINE ART PHOTOGRAPHY</span>
    </div>

    <div class="contact__name">Lukas Wendrovski</div>

    <div class="contact contact--social-a">
      <svg class="contact__icon" viewBox="0 0 17 17"><rect class="social-square" width="17" height="17" rx="3"/></svg>
      chirpline.com/vistaplume
    </div>
    <div class="contact contact--social-b">
      <svg class="contact__icon" viewBox="0 0 17 17"><rect class="social-square" width="17" height="17" rx="3"/></svg>
      friendpage.com/vistaplume
    </div>

    <div class="contact contact--phone">
      <svg class="contact__icon" viewBox="0 0 17 17" fill="none" stroke="#4a4b58" stroke-width="1.6">
        <rect x="4.5" y="1.5" width="8" height="14" rx="1.5"/>
        <line x1="6.5" y1="4.5" x2="10.5" y2="4.5"/>
        <line x1="6.5" y1="8" x2="10.5" y2="8"/>
        <line x1="6.5" y1="11" x2="10.5" y2="11"/>
      </svg>
      0415 309 662
    </div>
    <div class="contact contact--email">
      <svg class="contact__icon" viewBox="0 0 17 17">
        <rect x="1" y="4" width="15" height="10" fill="#4a4b58"/>
        <polyline points="1,4 8.5,10 16,4" fill="none" stroke="#fff" stroke-width="1.2"/>
      </svg>
      sales@vistaplume.com.au
    </div>
    <div class="contact contact--web">
      <svg class="contact__icon" viewBox="0 0 17 17" fill="none" stroke="#4a4b58" stroke-width="1.3">
        <circle cx="8.5" cy="8.5" r="7"/>
        <ellipse cx="8.5" cy="8.5" rx="3" ry="7"/>
        <line x1="1.5" y1="8.5" x2="15.5" y2="8.5"/>
        <line x1="2.5" y1="5" x2="14.5" y2="5"/>
        <line x1="2.5" y1="12" x2="14.5" y2="12"/>
      </svg>
      www.vistaplume.com.au
    </div>
  </section>
</body>
</html>
```